Expedition Cruise Sales Website for the Polar Regions (Antarctica & Arctic)

This will be a website for selling cruises.
This site should have a homepage, a ship page, destinations, and itineraries.
I have created a file specifying each page, and it is attached.
Pages:
1. Home
2. Cruise Lines
- 2.1 Ships
3. Destinations
- 3.1 Region - 3.2 Country - 3.3 City
4. Itineraries
- 4.1 Itinerary
5. Blog / Travel Tips 6. About Us
7. Contact
Please take a look on the attached pdf
Target Market(s)
Expedition Travelers
Coding
Coded - Design and coding required
Number of Pages Required
5+ page

```html
<!DOCTYPE html>
<html lang="en">
<head>
<meta charset="utf-8">
<title>Polarvoya – Expedition Cruises</title>
<link href="https://fonts.googleapis.com/css2?family=Poppins:ital,wght@0,400;0,500;0,600;0,700;1,400&display=swap" rel="stylesheet">
<style>
:root{
  --blue:#2f6bb5;
  --blue-deep:#1f4f8f;
  --ink:#161a22;
  --muted:#555c68;
  --line:#d9dee7;
  --pale:#f1f4fb;
  --white:#fff;
}
*{box-sizing:border-box;margin:0;padding:0}
html,body{width:1200px;height:4808px;overflow:hidden}
body{font-family:'Poppins',sans-serif;color:var(--ink);background:var(--white);position:relative}
.abs{position:absolute}
a{color:inherit;text-decoration:none}

/* header */
.site-header{position:absolute;left:0;top:0;width:1200px;height:140px;background:var(--white)}
.brand{position:absolute;left:127px;top:78px;font-size:32px;font-weight:600;color:var(--blue);display:flex;align-items:center;gap:10px}
.brand-dot{width:14px;height:14px;border-radius:50%;background:var(--blue)}
.login{position:absolute;left:735px;top:36px;font-size:16px;font-weight:500;display:flex;align-items:center;gap:8px}
.btn{display:inline-flex;align-items:center;justify-content:center;background:var(--blue);color:var(--white);font-weight:500;border-radius:4px}
.find-btn{position:absolute;left:915px;top:24px;width:157px;height:48px;font-size:16px}
.main-nav{position:absolute;left:327px;top:94px;display:flex;gap:38px;font-size:17px;font-weight:500}
.main-nav .active{color:var(--blue)}

/* hero */
.hero{position:absolute;left:0;top:140px;width:1200px;height:500px;background:linear-gradient(180deg,#aab9c8 0%,#6f8597 35%,#4c6474 60%,#3d6a92 78%,#2d5a85 100%)}
.hero-title{position:absolute;left:770px;top:300px;color:var(--white);font-weight:700;line-height:1}
.hero-title .small{font-size:38px;display:block}
.hero-title .big{font-size:58px;display:block;margin-top:2px}
.book-btn{position:absolute;left:768px;top:420px;width:132px;height:42px;font-size:16px;border:2px solid var(--white)}

.search-card{position:absolute;left:68px;top:527px;width:1064px;height:206px;background:var(--white);border-radius:14px;box-shadow:0 8px 24px rgba(0,0,0,.12)}
.search-card h2{position:absolute;left:0;width:100%;top:36px;text-align:center;font-size:26px;font-weight:500}
.field{position:absolute;top:101px;height:54px;border:1px solid var(--line);border-radius:4px;font-size:13px;display:flex;align-items:center;padding:0 10px;justify-content:space-between;color:var(--ink)}
.search-btn{position:absolute;left:868px;top:101px;width:168px;height:54px;font-size:17px}

/* sections */
.section-title{position:absolute;left:0;width:1200px;text-align:center;font-size:41px;font-weight:600}
.tabs{position:absolute;top:955px;left:237px;display:flex;gap:38px;font-size:19px;font-weight:500}
.tabs .active{color:var(--blue);border-bottom:2px solid var(--blue);padding:0 6px 8px}

.offer-card{position:absolute;width:292px;height:366px;background:var(--white);border:1px solid #e4e8ef;border-radius:6px;box-shadow:0 2px 10px rgba(0,0,0,.07);overflow:hidden}
.offer-card .photo{height:168px}
.offer-card h3{position:absolute;left:23px;top:188px;font-size:17px;font-weight:600;line-height:1.25;width:255px}
.offer-card .meta{position:absolute;left:23px;top:244px;font-size:13px}
.offer-card .price{position:absolute;left:23px;top:318px;font-size:17px;font-weight:600;color:var(--blue)}
.offer-card .price small{font-size:10px;color:var(--muted);font-weight:400}
.offer-card .go{position:absolute;right:22px;top:311px;width:40px;height:40px;border-radius:50%;background:#e9eef7;display:flex;align-items:center;justify-content:center}

.destinations{position:absolute;left:0;top:1470px;width:1200px;height:728px;background:var(--pale)}
.lede{position:absolute;left:0;width:1200px;text-align:center;font-size:15px;line-height:1.45}
.dest-card{position:absolute;width:295px;height:297px;border-radius:6px}
.dest-label{position:absolute;left:21px;top:250px;width:253px;height:67px;background:var(--blue);color:var(--white);font-size:19px;font-weight:600;display:flex;align-items:center;justify-content:center;border-radius:4px}

.about{position:absolute;left:0;top:2198px;width:1200px;height:514px;background:linear-gradient(90deg,#2f5f9c 0%,#4a76ac 40%,#8fa9c8 70%,#c7d4e2 100%)}
.about h2{position:absolute;left:210px;top:155px;color:var(--white);font-size:41px;font-weight:500}
.about p{position:absolute;left:127px;top:232px;width:335px;color:var(--white);font-size:15px;line-height:1.6}

.arrow{position:absolute;width:40px;height:40px;display:flex;align-items:center;justify-content:center}

.testimonials{position:absolute;left:0;top:3415px;width:1200px;height:613px;background:var(--pale)}
.t-card{position:absolute;top:225px;width:400px;height:283px;background:var(--white);border:1px solid #e1e5ee}
.avatar{position:absolute;left:32px;top:34px;width:62px;height:62px;border-radius:50%;background:#c9d3e0}
.t-name{position:absolute;left:118px;top:46px;font-size:14px;font-weight:600;color:var(--blue)}
.t-city{position:absolute;left:118px;top:68px;font-size:14px;font-weight:600}
.t-text{position:absolute;left:34px;top:115px;width:320px;font-size:14px;font-style:italic;color:var(--muted);line-height:1.55}
.stars{position:absolute;left:34px;top:225px;display:flex;gap:3px}
.round-arrow{position:absolute;top:3733px;width:40px;height:40px;border-radius:50%;background:var(--white);display:flex;align-items:center;justify-content:center;box-shadow:0 2px 6px rgba(0,0,0,.08)}

.newsletter{position:absolute;left:0;top:4028px;width:1200px;height:397px;background:linear-gradient(90deg,#2d64ad 0%,#3f77b9 45%,#89a9cf 100%)}
.newsletter h2{position:absolute;left:240px;top:90px;color:var(--white);font-size:33px;font-weight:600;line-height:1.2}
.newsletter p{position:absolute;left:238px;top:178px;width:440px;color:var(--white);font-size:16px;line-height:1.5}
.email{position:absolute;left:240px;top:244px;width:238px;height:50px;border:1px solid rgba(255,255,255,.85);border-radius:25px;color:var(--white);font-size:12px;display:flex;align-items:center;padding-left:18px}
.sub-btn{position:absolute;left:490px;top:242px;width:182px;height:50px;border-radius:25px;background:var(--white);color:var(--blue);font-size:17px;font-weight:500;display:flex;align-items:center;justify-content:center}
.penguin-scene{position:absolute;left:735px;top:60px;width:430px;height:300px;border-radius:50% 50% 40% 40%;background:radial-gradient(ellipse at center,#e6eef7 0%,#b9cbe0 55%,rgba(143,170,207,0) 75%)}

.site-footer{position:absolute;left:0;top:4425px;width:1200px;height:383px;background:linear-gradient(180deg,#dfe6ef 0%,#f2f5f9 50%,#e7ecf2 100%)}
.footer-brand{position:absolute;left:0;width:1200px;top:110px;text-align:center;font-size:27px;font-weight:500;color:var(--blue)}
.footer-nav{position:absolute;left:0;width:1200px;top:176px;display:flex;justify-content:center;gap:36px;font-size:15px}
.copyright{position:absolute;left:0;width:1200px;top:233px;text-align:center;font-size:14px}
.snow-figure{position:absolute;border-radius:40% 40% 20% 20%}
</style>
</head>
<body>

<header class="site-header">
  <div class="brand"><span class="brand-dot"></span>Polarvoya</div>
  <a class="login" href="#"><svg width="16" height="16" viewBox="0 0 16 16"><circle cx="8" cy="5" r="3.5" fill="#2f6bb5"/><path d="M1 16c0-4 3-6 7-6s7 2 7 6z" fill="#2f6bb5"/></svg>Login / Register</a>
  <a class="btn find-btn" href="#">Find A Cruise</a>
  <nav class="main-nav">
    <a class="active" href="#">Home</a><a href="#">Cruise Lines</a><a href="#">Destinations</a><a href="#">Itineraries</a><a href="#">Blog</a><a href="#">About Us</a><a href="#">Contact</a>
  </nav>
</header>

<section class="hero" role="img" aria-label="Expedition ship sailing a fjord beneath snowy mountains">
</section>
<div class="hero-title"><span class="small">Welcome to</span><span class="big">Polarvoya</span></div>
<a class="btn book-btn" href="#">Book Now</a>

<form class="search-card">
  <h2>Find Your Perfect Cruise at the Best Price</h2>
  <div class="field" style="left:27px;width:291px">Search Destinations/River</div>
  <div class="field" style="left:330px;width:168px">▭ Dates <span>⌄</span></div>
  <div class="field" style="left:512px;width:166px">▭ Days <span>⌄</span></div>
  <div class="field" style="left:687px;width:167px">Cruise Line <span>⌄</span></div>
  <div class="btn search-btn">Search Cruise</div>
</form>

<h2 class="section-title" style="top:870px">Featured Offers</h2>
<div class="tabs"><span class="active">Best Antarctic Cruises</span><span>Top Galápagos Cruises</span><span>Last Minute Deals</span></div>

<article class="offer-card" style="left:128px;top:1037px"><div class="photo" role="img" aria-label="Cruise ship near snowy peaks" style="background:linear-gradient(180deg,#c3d3e3,#6a87a3)"></div><h3>Lorem ipsum dolor sit amet onsectetur adipiscing</h3><p class="meta">9 days |&nbsp; 10 days</p><p class="price">from € 1,399 <small>/ Person</small></p><span class="go"><svg width="10" height="14" viewBox="0 0 10 14"><path d="M2 1l6 6-6 6" stroke="#2f6bb5" stroke-width="1.6" fill="none"/></svg></span></article>
<article class="offer-card" style="left:455px;top:1037px"><div class="photo" role="img" aria-label="Cruise ship among icebergs" style="background:linear-gradient(180deg,#5a86c0,#1d3f6b)"></div><h3>Lorem ipsum dolor sit amet onsectetur adipiscing</h3><p class="meta">9 days |&nbsp; 10 days</p><p class="price">from € 1,399 <small>/ Person</small></p><span class="go"><svg width="10" height="14" viewBox="0 0 10 14"><path d="M2 1l6 6-6 6" stroke="#2f6bb5" stroke-width="1.6" fill="none"/></svg></span></article>
<article class="offer-card" style="left:781px;top:1037px"><div class="photo" role="img" aria-label="Cruise ship beside a glacier" style="background:linear-gradient(180deg,#d5e3f0,#88a8c6)"></div><h3>Lorem ipsum dolor sit amet onsectetur adipiscing</h3><p class="meta">9 days |&nbsp; 10 days</p><p class="price">from € 1,399 <small>/ Person</small></p><span class="go"><svg width="10" height="14" viewBox="0 0 10 14"><path d="M2 1l6 6-6 6" stroke="#2f6bb5" stroke-width="1.6" fill="none"/></svg></span></article>

<section class="destinations">
  <h2 class="section-title" style="top:140px">Destinations</h2>
  <p class="lede" style="top:202px">Lorem ipsum dolor sit amet, consectetur adipiscing elit, sed do eiusmod<br>tempor incididunt ut labore et dolore magna aliquais iendiss.</p>
  <div class="dest-card" style="left:127px;top:293px;background:linear-gradient(180deg,#8fb3d8,#3c5878)" role="img" aria-label="City skyline with twin towers"><div class="dest-label">Destination Name</div></div>
  <div class="dest-card" style="left:453px;top:293px;background:linear-gradient(180deg,#7aa0c8,#2e5f90)" role="img" aria-label="Arched iceberg in the sea"><div class="dest-label">Destination Name</div></div>
  <div class="dest-card" style="left:778px;top:293px;background:linear-gradient(180deg,#cfdff0,#9bb7d4)" role="img" aria-label="Polar bear walking on sea ice"><div class="dest-label">Destination Name</div></div>
</section>

<section class="about" role="img" aria-label="Penguins and a polar bear on ice with a cruise ship and iceberg behind">
  <h2>About Us</h2>
  <p>Lorem ipsum dolor sit amet, consectetur adipiscing elit, sed do eiusmod tempor incididunt ut labore et dolore magna aliq ua. Quis ipsum suspendisse ultrices grav ida. Risus commodo viverra maecenas accumsan lacus vel facilisis.</p>
</section>

<h2 class="section-title" style="top:2842px">Cruise Line</h2>
<span class="arrow" style="left:68px;top:2990px"><svg width="16" height="30" viewBox="0 0 16 30"><path d="M14 2L2 15l12 13" stroke="#2f6bb5" stroke-width="2" fill="none"/></svg></span>
<span class="arrow" style="left:1092px;top:2990px"><svg width="16" height="30" viewBox="0 0 16 30"><path d="M2 2l12 13L2 28" stroke="#2f6bb5" stroke-width="2" fill="none"/></svg></span>
<article class="offer-card" style="left:128px;top:2930px"><div class="photo" role="img" aria-label="Cruise ship near ice shelf" style="background:linear-gradient(180deg,#a9c2dc,#e4ecf4)"></div><h3>Lorem ipsum dolor sit amet onsectetur adipiscing</h3><p class="meta">9 days |&nbsp; 10 days</p><p class="price">from € 1,399 <small>/ Person</small></p><span class="go"><svg width="10" height="14" viewBox="0 0 10 14"><path d="M2 1l6 6-6 6" stroke="#2f6bb5" stroke-width="1.6" fill="none"/></svg></span></article>
<article class="offer-card" style="left:455px;top:2930px"><div class="photo" role="img" aria-label="Red-hulled ship between ice walls" style="background:linear-gradient(180deg,#c7dbee,#5f88b5)"></div><h3>Lorem ipsum dolor sit amet onsectetur adipiscing</h3><p class="meta">9 days |&nbsp; 10 days</p><p class="price">from € 1,399 <small>/ Person</small></p><span class="go"><svg width="10" height="14" viewBox="0 0 10 14"><path d="M2 1l6 6-6 6" stroke="#2f6bb5" stroke-width="1.6" fill="none"/></svg></span></article>
<article class="offer-card" style="left:781px;top:2930px"><div class="photo" role="img" aria-label="Ship in front of snowy mountains" style="background:linear-gradient(180deg,#d0dae4,#6f8496)"></div><h3>Lorem ipsum dolor sit amet onsectetur adipiscing</h3><p class="meta">9 days |&nbsp; 10 days</p><p class="price">from € 1,399 <small>/ Person</small></p><span class="go"><svg width="10" height="14" viewBox="0 0 10 14"><path d="M2 1l6 6-6 6" stroke="#2f6bb5" stroke-width="1.6" fill="none"/></svg></span></article>

<section class="testimonials">
  <h2 class="section-title" style="top:125px">Customer Testimonials</h2>
  <div class="t-card" style="left:200px"><div class="avatar" role="img" aria-label="Customer portrait"></div><p class="t-name">ELIN MARSH</p><p class="t-city">City Name</p><p class="t-text">Lorem ipsum dolor sit amet, consectetur adipiscing elit, sed do eiusmod tempor incididunt ut labore et dolore magaua uis ipsum suspendisse ultrices.</p><div class="stars"><svg width="112" height="20" viewBox="0 0 112 20" fill="#2f6bb5"><g id="st"><path d="M10 1l2.6 6 6.4.5-4.9 4.2 1.5 6.3L10 14.6 4.4 18l1.5-6.3L1 7.5l6.4-.5z"/></g><use href="#st" x="23"/><use href="#st" x="46"/><use href="#st" x="69"/><use href="#st" x="92"/></svg></div></div>
  <div class="t-card" style="left:623px"><div class="avatar" role="img" aria-label="Customer portrait"></div><p class="t-name">ELIN MARSH</p><p class="t-city">City Name</p><p class="t-text">Lorem ipsum dolor sit amet, consectetur adipiscing elit, sed do eiusmod tempor incididunt ut labore et dolore magaua uis ipsum suspendisse ultrices.</p><div class="stars"><svg width="112" height="20" viewBox="0 0 112 20" fill="#2f6bb5"><use href="#st"/><use href="#st" x="23"/><use href="#st" x="46"/><use href="#st" x="69"/><use href="#st" x="92"/></svg></div></div>
</section>
<span class="round-arrow" style="left:95px"><svg width="8" height="14" viewBox="0 0 8 14"><path d="M7 1L1 7l6 6" stroke="#2f6bb5" stroke-width="1.4" fill="none"/></svg></span>
<span class="round-arrow" style="left:1062px"><svg width="8" height="14" viewBox="0 0 8 14"><path d="M1 1l6 6-6 6" stroke="#2f6bb5" stroke-width="1.4" fill="none"/></svg></span>

<section class="newsletter">
  <div class="penguin-scene" role="img" aria-label="Penguins standing on a floating ice floe"></div>
  <h2>Get Cruise Deals Directly<br>In Your Inbox</h2>
  <p>Subscribe now and set sail on a journey of endless adventure with our exclusive cruise newsletter.</p>
  <div class="email">Email Id</div>
  <div class="sub-btn">Subscribe Now</div>
</section>

<footer class="site-footer">
  <div class="snow-figure" style="left:85px;top:110px;width:145px;height:270px;background:linear-gradient(180deg,#3a3f48,#d7dce3)" role="img" aria-label="Penguin standing in snow"></div>
  <div class="snow-figure" style="left:1005px;top:160px;width:155px;height:215px;background:linear-gradient(180deg,#e6dcc6,#cbbd9f)" role="img" aria-label="Polar bear sitting in snow"></div>
  <div class="footer-brand">Polarvoya</div>
  <nav class="footer-nav"><a href="#">Home</a><a href="#">Cruise Lines</a><a href="#">Destinations</a><a href="#">Itineraries</a><a href="#">Blog</a><a href="#">About Us</a><a href="#">Contact</a></nav>
  <p class="copyright">Copyright © 2020 Polarvoya All Rights Reserved.</p>
</footer>

</body>
</html>
```